Harbor & Crest Real estate

Design of business plans and presentations before and after of assets is required.
The design is of PowerPoint files and needs to be tailored to the US real estate market.
Graphs and relevant information is required about the area where the company property, Cincinnati Ohio is located.
To get acquainted with the logo, colors and guidelines of the existing company design, visit the website- www.hcqholdings.com

Seeking designer for long term collaborative work.

Font styles to use
Sans Serif

```html
<!DOCTYPE html>
<html lang="en">
<head>
<meta charset="utf-8">
<title>Harrison Project – Plans vs. Execution</title>
<link href="https://fonts.googleapis.com/css2?family=Rubik:wght@500;700;800&family=Hind:wght@400;500;600&family=Crimson+Text:wght@400&display=swap" rel="stylesheet">
<style>
:root{
  --bg:#e6e6e4;
  --ink:#161616;
  --yellow:#f9cb2e;
  --paper:#ffffff;
  --grey:#8c8c8c;
  --line:#d8d8d8;
  --photo-warm:#b9a98c;
  --photo-cool:#8fa0ad;
}
*{box-sizing:border-box;margin:0;padding:0}
html,body{width:1200px;height:847px;overflow:hidden;background:var(--bg)}
body{position:relative;font-family:"Hind",sans-serif;color:var(--ink)}
.page{position:absolute;width:254px;height:364px;background:var(--paper);overflow:hidden;box-shadow:0 1px 4px rgba(0,0,0,.12)}
.page > *{position:absolute}
.abs{position:absolute}
.heading{font-family:"Rubik",sans-serif;font-weight:800;line-height:1}
.body-text{font-size:4.6px;line-height:1.5;color:#333}
.serif{font-family:"Crimson Text",serif;font-size:5.6px;line-height:1.25;color:#222}
.photo{background:linear-gradient(135deg,var(--photo-warm),#6f6655)}
.photo.cool{background:linear-gradient(160deg,#9fb5c6,#7a7f6e)}
.photo.room{background:linear-gradient(160deg,#d9d2c4,#8d7a62)}
.footer{left:0;bottom:0;width:100%;height:7px;background:var(--ink)}
.footer span{position:absolute;right:4px;top:0;height:7px;width:30px;background:var(--yellow);font-size:3.6px;line-height:7px;text-align:center;color:var(--ink)}
.bullet-icon{width:13px;height:13px}
.label-bar{background:var(--yellow);font-family:"Rubik",sans-serif;font-weight:500;font-size:6px;line-height:15px;padding-left:13px}
.data-table{background:#fff;font-size:3.8px;line-height:7.1px}
.data-table .row{display:flex;justify-content:space-between;padding:0 5px;color:#333}
.data-table .row:nth-child(odd){background:#fdf1c4}
.tl-dot{width:7px;height:7px;border-radius:50%;background:var(--ink);border:1.5px solid #fff;box-shadow:0 0 0 1px var(--ink)}
.tl-icon{border-radius:50%;background:var(--yellow);border:2px solid #fff;box-shadow:0 0 0 1.5px var(--yellow)}
.tl-icon::after{content:"";position:absolute;left:50%;top:50%;width:38%;height:38%;transform:translate(-50%,-50%);background:#fff;border:1px solid var(--ink);border-radius:2px}
.tl-icon.dark{background:var(--yellow);box-shadow:0 0 0 3px var(--ink)}
.q{font-family:"Rubik",sans-serif;font-weight:700;font-size:6px}
</style>
</head>
<body>

<!-- Cover -->
<section class="page cover" style="left:66px;top:53px;background:#1c1c1c">
  <svg class="abs" style="left:0;top:0" width="254" height="364" viewBox="0 0 254 364">
    <rect x="0" y="244" width="254" height="120" fill="var(--yellow)"/>
    <polygon points="0,240 95,145 160,210 0,370" fill="#101010"/>
    <polygon points="20,300 128,192 200,264 90,374" fill="#101010"/>
    <polygon points="140,60 254,174 254,250 100,96" fill="#101010"/>
  </svg>
  <div class="abs photo" role="img" aria-label="Photo of a two-storey wooden house with porch and front lawn" style="left:48px;top:100px;width:160px;height:160px;transform:rotate(45deg);background:linear-gradient(180deg,#6f9ad0 0%,#c9b48a 45%,#7a6a4c 70%,#4f7a34 100%)"></div>
  <div class="abs heading" style="left:184px;top:34px;color:#fff;font-size:6.5px;font-weight:500;font-family:'Rubik',sans-serif">Harbor &amp; Crest</div>
  <div class="abs heading" style="left:0;width:254px;top:282px;text-align:center;color:#fff;font-size:24px">Harrison Project</div>
  <div class="abs" style="left:0;width:254px;top:311px;text-align:center;color:#fff;font-family:'Rubik',sans-serif;font-size:8.5px;letter-spacing:3.2px">PLANS VS. EXECUTION</div>
</section>

<!-- Background page -->
<section class="page" style="left:342px;top:53px">
  <svg class="abs" style="left:0;top:0" width="258" height="75" viewBox="0 0 258 75">
    <polygon points="0,0 155,0 100,72 0,72" fill="var(--ink)"/>
    <polygon points="155,0 258,0 258,14 115,48" fill="var(--yellow)"/>
  </svg>
  <div class="heading" style="left:18px;top:16px;color:#fff;font-size:13px;line-height:1.05">Harrison<br>Project</div>
  <div style="left:33px;top:78px;font-size:6px;font-weight:600">Background:</div>
  <svg class="abs" style="left:20px;top:118px" width="14" height="260" viewBox="0 0 14 260">
    <g fill="none" stroke="var(--yellow)" stroke-width="1.2">
      <circle cx="7" cy="7" r="6"/><path d="M5.5 4.5 8 7 5.5 9.5"/>
      <circle cx="7" cy="59" r="6"/><path d="M5.5 56.5 8 59 5.5 61.5"/>
      <circle cx="7" cy="104" r="6"/><path d="M5.5 101.5 8 104 5.5 106.5"/>
      <circle cx="7" cy="149" r="6"/><path d="M5.5 146.5 8 149 5.5 151.5"/>
      <circle cx="7" cy="203" r="6"/><path d="M5.5 200.5 8 203 5.5 205.5"/>
    </g>
  </svg>
  <p class="serif" style="left:45px;top:105px;width:195px">Harbor &amp; Crest is an investment and real estate management company for U.S. assets specializing in providing significant and comprehensive benefits to its investors across the entire value chain of their investment from location, betterment and renovation, ongoing management and sales management.</p>
  <p class="serif" style="left:45px;top:164px;width:195px">The core of our real estate investment conduct lies first and foremost in locating transactions at the right price, with the central ambition being to locate assets at prices significantly lower than the market price.</p>
  <p class="serif" style="left:45px;top:212px;width:195px">Over the years, we have developed a unique method for locating Value Add assets in the activity areas at prices below market prices.</p>
  <p class="serif" style="left:45px;top:248px;width:195px">Today, the company manages over 500 properties and units in the United States, properties it has fully developed (locating purchasing renovating and building operating and managing).</p>
  <p class="serif" style="left:45px;top:286px;width:195px">The company's team is made up entirely of company employees from construction workers to management enabling us to manage the transaction alongside a plan vs. execution model and to save on cost improvement and maximizing the overall return.</p>
  <div class="footer"><span>Page | 2</span></div>
</section>

<!-- Locating the transaction -->
<section class="page" style="left:619px;top:53px">
  <svg class="abs" style="left:0;top:190px" width="254" height="174" viewBox="0 0 254 174"><polygon points="70,0 150,80 70,160 -10,80" fill="#f1f1f1"/></svg>
  <div style="left:0;top:0;width:254px;height:23px;background:var(--ink)"></div>
  <div class="heading" style="left:0;width:254px;top:33px;text-align:center;font-size:14px;font-weight:700">Locating the transaction</div>
  <div class="photo" role="img" aria-label="Street map of the western Cincinnati neighbourhoods" style="left:0;top:61px;width:115px;height:80px;background:linear-gradient(135deg,#e9ece8,#d6dde2 60%,#cfe0cd)"></div>
  <p class="body-text" style="left:126px;top:60px;width:118px;text-align:justify">Our locating system focuses on yielding assets with potential for improvement that are either partially occupied or upgradeable when the objective is to purchase assets below market price.</p>
  <div style="left:126px;top:101px;width:118px;height:0.6px;background:var(--yellow)"></div>
  <p class="body-text" style="left:126px;top:110px;width:118px;text-align:justify">The properties are located in developing areas and neighborhoods, close to top schools, universities, employment centers and major transport hubs.</p>
  <p class="body-text" style="left:16px;top:152px;width:224px">Within the locating system, we have developed unique methods for locating assets that do not exist or are not offered on the market for sale, and thus the brokerage price gaps can be saved.</p>
  <div style="left:16px;top:180px;width:228px;height:0.6px;background:var(--line)"></div>
  <p class="body-text" style="left:16px;top:188px;width:228px"><b>The Harrison 1840 Project</b> was located through locator Daniel Reeves, who focused on the Westwood neighborhood, a central neighborhood among the three western neighborhoods in Cincinnati.</p>
  <div style="left:16px;top:217px;width:228px;height:0.6px;background:var(--line)"></div>
  <p class="body-text" style="left:16px;top:227px;width:100px;text-align:justify">After Daniel surveyed the area, he decided to focus his efforts on the central axis, Harrison Street, which runs through the three western neighborhoods mentioned above.</p>
  <p class="body-text" style="left:16px;top:279px;width:100px">The property located is a multi family with 18 housing units, with partial occupancy and considerable betterment potential.</p>
  <div class="photo" role="img" aria-label="Aerial photo of a wooded residential neighbourhood" style="left:127px;top:243px;width:127px;height:81px;background:linear-gradient(160deg,#7d8a6a,#55624a 50%,#8a8d80)"></div>
  <div style="left:127px;top:324px;width:127px;height:11px;background:var(--yellow)"></div>
  <div class="footer"><span>Page | 3</span></div>
</section>

<!-- Plans -->
<section class="page" style="left:896px;top:253px;height:363px">
  <div style="left:0;top:0;width:135px;height:37px;background:var(--ink)"></div>
  <div class="heading" style="left:14px;top:12px;color:var(--yellow);font-size:18px;font-weight:700">Plans</div>
  <div style="left:0;top:37px;width:254px;height:102px;background:var(--yellow)"></div>
  <div class="body-text" style="left:16px;top:42px;width:226px;color:var(--ink);font-size:4.4px">
    <p>Value Add Investment Strategy: Built on the acquisition of assets tens of percent below their value using the Off Market method.</p>
    <p style="margin-top:5px">The plan is to acquire the property, better it by renovating all the units and the common space, and house the units at the accepted market rent prices.</p>
    <p style="margin-top:5px">After the raising of rents, ongoing management and maintenance will be done efficiently and economically in such a way that significantly reduces the cost of the complex and significantly improves the profit margins.</p>
    <p style="margin-top:5px">Towards the end of the process, the cash flow from the project will increase and generate higher profits, thus increasing the value of the property.</p>
  </div>
  <div style="left:0;top:141px;width:135px;height:222px;background:var(--ink)"></div>
  <div class="heading" style="left:17px;top:162px;color:#fff;font-size:8.5px;font-weight:500;line-height:1.3">ASSET STATUS AT<br>LOCATION TIME</div>
  <div class="body-text" style="left:145px;top:148px;font-size:5px;line-height:1.35;color:#222">Occupancy rate 66<br><br>Net monthly income<br>$ 3,600</div>
  <div style="left:145px;top:181px;width:109px;height:20px;background:var(--yellow)"></div>
  <div class="body-text" style="left:147px;top:181px;font-size:5px;line-height:1.35;color:#222">Purchase price after negotiation<br><b style="font-size:6px">$ 475,000</b></div>
  <div role="img" aria-label="Scanned settlement statement form" style="left:11px;top:210px;width:226px;height:145px;background:#fff;border:0.6px solid #555">
    <div class="abs" style="left:3px;top:3px;font-size:4px;font-weight:600">A. Settlement Statement</div>
    <svg class="abs" style="left:0;top:0" width="226" height="145" viewBox="0 0 226 145">
      <g stroke="#444" stroke-width="0.4">
        <line x1="0" y1="12" x2="226" y2="12"/><line x1="0" y1="24" x2="226" y2="24"/>
        <line x1="0" y1="34" x2="226" y2="34"/><line x1="0" y1="48" x2="226" y2="48"/>
        <line x1="0" y1="62" x2="226" y2="62"/><line x1="0" y1="74" x2="226" y2="74"/>
        <line x1="0" y1="88" x2="226" y2="88"/><line x1="0" y1="100" x2="226" y2="100"/>
        <line x1="0" y1="112" x2="226" y2="112"/><line x1="0" y1="124" x2="226" y2="124"/>
        <line x1="0" y1="136" x2="226" y2="136"/><line x1="34" y1="34" x2="34" y2="112"/>
        <line x1="113" y1="112" x2="113" y2="145"/>
      </g>
      <g stroke="#999" stroke-width="0.3">
        <line x1="38" y1="40" x2="190" y2="40"/><line x1="38" y1="54" x2="170" y2="54"/>
        <line x1="38" y1="68" x2="160" y2="68"/><line x1="38" y1="80" x2="200" y2="80"/>
        <line x1="38" y1="94" x2="150" y2="94"/><line x1="38" y1="106" x2="210" y2="106"/>
        <line x1="4" y1="118" x2="100" y2="118"/><line x1="117" y1="118" x2="210" y2="118"/>
        <line x1="4" y1="130" x2="100" y2="130"/><line x1="117" y1="130" x2="210" y2="130"/>
      </g>
      <ellipse cx="140" cy="121" rx="13" ry="4" fill="none" stroke="var(--yellow)" stroke-width="1.2"/>
      <line x1="152" y1="118" x2="190" y2="97" stroke="var(--yellow)" stroke-width="1"/>
    </svg>
  </div>
  <div style="left:190px;top:268px;width:46px;height:46px;border-radius:50%;background:#fff;box-shadow:0 0 4px rgba(0,0,0,.25);font-size:4.6px;line-height:1.2;text-align:center;padding-top:14px">Cost of<br>purchasing<br>asset</div>
  <div class="footer"><span>Page | 4</span></div>
</section>

<!-- Business plan expectations -->
<section class="page" style="left:66px;top:434px">
  <svg class="abs" style="left:0;top:0" width="254" height="50" viewBox="0 0 254 50">
    <polygon points="0,0 195,0 160,49 0,49" fill="var(--ink)"/>
    <polygon points="195,0 254,0 254,10 168,38" fill="var(--yellow)"/>
  </svg>
  <div class="heading" style="left:16px;top:12px;color:#fff;font-size:10px;font-weight:700;line-height:1.3">Business Plan<br>Expectations</div>
  <div style="left:28px;top:57px;font-family:'Rubik',sans-serif;font-weight:500;font-size:6.3px">RENOVATION AND BUDGET PLAN</div>
  <div style="left:0;top:64px;width:19px;height:90px;background:var(--ink)"></div>
  <svg class="abs" style="left:13px;top:70px" width="12" height="70" viewBox="0 0 12 70">
    <g fill="#fff" stroke="var(--yellow)" stroke-width="1.1">
      <circle cx="6" cy="6" r="5"/><circle cx="6" cy="23.5" r="5"/><circle cx="6" cy="41.5" r="5"/><circle cx="6" cy="60" r="5"/>
    </g>
    <g fill="none" stroke="var(--yellow)" stroke-width="1"><path d="M5 4 7 6 5 8"/><path d="M5 21.5 7 23.5 5 25.5"/><path d="M5 39.5 7 41.5 5 43.5"/><path d="M5 58 7 60 5 62"/></g>
  </svg>
  <div class="serif" style="left:28px;top:72px;font-size:6.3px;line-height:18.2px">Replacing roof<br>Replacing windows<br>Renovation of units, kitchens and bathrooms and toilets<br>Renewal of electrical appliances</div>
  <div style="left:29px;top:141px;font-size:6.4px;font-weight:600">HVAC replacementBudget:&nbsp; $138,000</div>
  <div style="left:19px;top:154px;width:235px;height:84px;background:var(--yellow)"></div>
  <div style="left:27px;top:168px;transform:rotate(-90deg);transform-origin:left top;top:220px;font-family:'Rubik',sans-serif;font-weight:700;font-size:6.5px;color:#fff;width:60px">4 KEY DATA</div>
  <div class="data-table" style="left:44px;top:163px;width:201px;height:75px;padding-top:4px">
    <div class="row"><span>Expected total cost</span><span>$613.000</span></div>
    <div class="row"><span>Expected Gross income (year)</span><span>$118,800</span></div>
    <div class="row"><span>Expected net income (year)</span><span>$59,400</span></div>
    <div class="row"><span>Expected net return</span><span>9.69%</span></div>
    <div class="row"><span>Expected net income (month)</span><span>$4,950</span></div>
    <div class="row"><span>Betterment length (months)</span><span>6</span></div>
    <div class="row"><span>Housing length after betterment (months)</span><span>2</span></div>
  </div>
  <div style="left:18px;top:246px;font-size:5.6px;font-weight:600">Project Timeline (Acquisition, Betterment, Housing and Stabilization)</div>
  <div class="q" style="left:43px;top:260px">Q1</div><div class="q" style="left:98px;top:260px">Q2</div>
  <div class="q" style="left:154px;top:260px">Q3</div><div class="q" style="left:208px;top:260px">Q4</div>
  <div style="left:24px;top:279px;width:215px;border-top:1px dotted var(--yellow)"></div>
  <div class="tl-dot" style="left:44px;top:276px"></div><div class="tl-dot" style="left:99px;top:276px"></div>
  <div class="tl-dot" style="left:155px;top:276px"></div><div class="tl-dot" style="left:209px;top:276px"></div>
  <div class="tl-icon" style="left:10px;top:293px;width:30px;height:30px"></div>
  <div class="tl-icon" style="left:86px;top:293px;width:30px;height:30px"></div>
  <div class="tl-icon" style="left:130px;top:293px;width:30px;height:30px"></div>
  <div style="left:8px;top:330px;font-size:4.2px;line-height:1.25;font-weight:600">Recruitment and<br>completion of the<br>acquisition</div>
  <div style="left:84px;top:330px;font-size:4.2px;line-height:1.25;font-weight:600">Completion of<br>renovation and<br>betterment</div>
  <div style="left:129px;top:330px;font-size:4.2px;line-height:1.25;font-weight:600">Housing and<br>ongoing<br>management</div>
  <div class="footer"><span>Page | 5</span></div>
</section>

<!-- Execution -->
<section class="page" style="left:342px;top:434px">
  <div class="heading" style="left:0;width:254px;top:12px;text-align:center;font-size:19px;font-weight:500">Execution</div>
  <div class="label-bar" style="left:0;top:33px;width:93px;height:15px">Before renovations</div>
  <div class="photo room" role="img" aria-label="Interior before renovation: kitchen with air conditioner" style="left:0;top:48px;width:67px;height:63px"></div>
  <div class="photo cool" role="img" aria-label="Interior before renovation: bathroom tiles" style="left:0;top:112px;width:67px;height:66px"></div>
  <div class="photo" role="img" aria-label="Interior before renovation: carpeted staircase" style="left:68px;top:48px;width:92px;height:130px;background:linear-gradient(180deg,#e4ddcf,#6b4d33)"></div>
  <div class="photo" role="img" aria-label="Interior before renovation: damaged wall with mould" style="left:162px;top:48px;width:92px;height:130px;background:linear-gradient(160deg,#cfc8b8,#5d574b)"></div>
  <div class="label-bar" style="left:0;top:201px;width:93px;height:15px">Before renovations</div>
  <div class="photo" role="img" aria-label="Furnished living room" style="left:0;top:204px;width:129px;height:71px;background:linear-gradient(160deg,#d8d2cc,#8b4e3f)"></div>
  <div class="photo room" role="img" aria-label="Empty room with wooden floor" style="left:0;top:276px;width:55px;height:62px"></div>
  <div class="photo" role="img" aria-label="Renovated wooden staircase" style="left:58px;top:276px;width:71px;height:62px;background:linear-gradient(160deg,#ece6dc,#7a5634)"></div>
  <div class="photo" role="img" aria-label="Brick apartment building exterior under blue sky" style="left:133px;top:204px;width:121px;height:134px;background:linear-gradient(180deg,#3b7bd4 0%,#9bc0ea 35%,#b59463 55%,#6d5a3f 100%)"></div>
  <div class="footer"><span>Page | 6</span></div>
</section>

<!-- Plans vs. execution -->
<section class="page" style="left:619px;top:434px">
  <svg class="abs" style="left:0;top:0" width="254" height="50" viewBox="0 0 254 50">
    <polygon points="0,0 195,0 160,49 0,49" fill="var(--ink)"/>
    <polygon points="195,0 254,0 254,10 168,38" fill="var(--yellow)"/>
  </svg>
  <div class="heading" style="left:15px;top:14px;color:#fff;font-size:10px;font-weight:700">Plans Vs. Execution</div>
  <div style="left:12px;top:48px;font-family:'Rubik',sans-serif;font-weight:500;font-size:6.8px">TIMELINE - PLANS VS. EXECUTION</div>
  <div style="left:0;top:61px;width:102px;height:29px;background:var(--ink);color:#fff;font-family:'Rubik',sans-serif;font-weight:500;font-size:7px;line-height:29px;padding-left:33px">Plans</div>
  <div class="serif" style="left:102px;top:61px;width:152px;height:29px;background:var(--yellow);font-size:5px;line-height:1.2;padding:7px 6px 0">The duration for the renovation and betterment process according to the business plan was 6 months.</div>
  <div class="tl-icon" style="left:14px;top:100px;width:28px;height:28px"></div>
  <div class="tl-icon" style="left:94px;top:96px;width:28px;height:28px"></div>
  <div class="tl-icon" style="left:131px;top:96px;width:28px;height:28px"></div>
  <div class="q" style="left:46px;top:135px">Q1</div><div class="q" style="left:100px;top:135px">Q2</div>
  <div class="q" style="left:155px;top:136px">Q3</div><div class="q" style="left:210px;top:135px">Q4</div>
  <div style="left:26px;top:148px;width:220px;border-top:1px dotted var(--yellow)"></div>
  <div class="tl-dot" style="left:48px;top:145px"></div><div class="tl-dot" style="left:102px;top:145px"></div>
  <div class="tl-dot" style="left:157px;top:145px"></div><div class="tl-dot" style="left:212px;top:145px"></div>
  <div class="tl-icon dark" style="left:47px;top:163px;width:28px;height:28px"></div>
  <div class="tl-icon dark" style="left:82px;top:163px;width:28px;height:28px"></div>
  <div style="left:0;top:203px;width:102px;height:27px;background:var(--ink);color:#fff;font-family:'Rubik',sans-serif;font-weight:500;font-size:7px;line-height:27px;padding-left:28px">Execution</div>
  <div class="serif" style="left:102px;top:203px;width:152px;height:27px;background:var(--yellow);font-size:4.8px;line-height:1.2;padding:3px 6px 0">In reality, property betterment took 4 months and full re-occupancy took only 1 month from the end of the renovation process!</div>
  <div style="left:13px;top:240px;font-family:'Rubik',sans-serif;font-weight:500;font-size:6.8px">SUMMARY TABLE - TIMELINE - PLANS VS. EXECUTION</div>
  <div style="left:9px;top:250px;width:240px;height:104px;background:var(--yellow)"></div>
  <div style="left:9px;top:251px;width:113px;text-align:center;font-family:'Rubik',sans-serif;font-weight:500;font-size:5.5px">Business Plan Expectations</div>
  <div style="left:129px;top:251px;width:114px;text-align:center;font-family:'Rubik',sans-serif;font-weight:500;font-size:5.5px">Actual Performance</div>
  <div class="data-table" style="left:12px;top:259px;width:113px;height:91px;font-size:3.6px;line-height:9.5px">
    <div style="text-align:center;font-weight:600;font-size:4.2px">Key Data</div>
    <div class="row"><span>Expected total cost</span><span>$613.000</span></div>
    <div class="row"><span>Expected Gross income (year)</span><span>$118,800</span></div>
    <div class="row"><span>Expected net income (year)</span><span>$59,400</span></div>
    <div class="row"><span>Expected net return</span><span>9.69%</span></div>
    <div class="row"><span>Expected net income (month)</span><span>$4,950</span></div>
    <div class="row"><span>Betterment length (months)</span><span>6</span></div>
    <div class="row"><span>Housing length after betterment</span><span>2</span></div>
  </div>
  <div class="data-table" style="left:132px;top:259px;width:114px;height:91px;font-size:3.6px;line-height:9.5px">
    <div style="text-align:center;font-weight:600;font-size:4.2px">Key Data</div>
    <div class="row"><span>Expected total cost</span><span>$613.000</span></div>
    <div class="row"><span>Expected Gross income (year)</span><span>$129,600</span></div>
    <div class="row"><span>Expected net income (year)</span><span>$77,760</span></div>
    <div class="row"><span>Expected net return</span><span>12.69%</span></div>
    <div class="row"><span>Expected net income (month)</span><span>$6,480</span></div>
    <div class="row"><span>Betterment length (months)</span><span>4</span></div>
    <div class="row"><span>Housing length after betterment</span><span>1</span></div>
  </div>
  <div class="footer"><span>Page | 7</span></div>
</section>

</body>
</html>
```